A5 Flyer for Financial Services Business

I am after a re-design of our business flyer to fit in with our new branding style and logo colour scheme. Wanting something with a bit of designer flair that I could not create myself. I have included the flyer which I created which lacks style so dazzle me.

I want to use the same content.

Text for main body of flyer is

Are you a small business owner, tradie or PAVC Service Provider struggling to stay on top of your bookkeeping and compliance obligations? If so we would love to help you get back on track and take control of your business finances so that you can make informed business decisions and focus on what you do best.

We have over 20 years industry experience and, as a small business ourselves, we are able to offer our clients a personal bookkeeping solution tailored to meet the needs of your business.

Accounts Payable | Accounts Receivable
Customer Invoicing
Bank and Credit Card Reconciliations
Payroll | Superannuation | Payroll Tax
Business Activity | Instalment Activity Statements
Regular Financial Reports
Ledgra and Tallybooks Set-Up and Training

```html
<!DOCTYPE html>
<html lang="en">
<head>
<meta charset="utf-8">
<title>Even Keel Financial Services – Bookkeeping Flyer</title>
<link rel="stylesheet" href="https://fonts.googleapis.com/css2?family=Montserrat:wght@400;500;600;700&display=swap">
<style>
  :root{
    --page:#eceeef;
    --paper:#f3f4f5;
    --charcoal:#3a3d40;
    --text:#3b3f44;
    --band:#d8dbdc;
    --teal:#3fd19a;
    --teal-deep:#1f9c8e;
    --navy:#1e3a4d;
    --brand:#2b5f73;
    --white:#ffffff;
  }
  *{box-sizing:border-box;margin:0;padding:0}
  html,body{width:1200px;height:849px;overflow:hidden;background:var(--page)}
  body{font-family:"Montserrat",sans-serif;color:var(--text);position:relative}
  .flyer{
    position:absolute;left:320px;top:28px;width:560px;height:792px;
    background:linear-gradient(180deg,#f7f8f8 0%,var(--paper) 60%,#eef0f1 100%);
    overflow:hidden;box-shadow:0 6px 18px rgba(0,0,0,.18);
  }
  .hero-art{position:absolute;left:0;top:0}
  .brand{
    position:absolute;left:30px;top:52px;width:210px;text-align:center;
    color:var(--brand);font-weight:500;
  }
  .brand-mark{display:block;width:30px;height:30px;margin:0 auto 10px;background:var(--brand)}
  .brand-name{display:block;font-size:24px;letter-spacing:.5px;line-height:1.1}
  .brand-sub{display:block;font-size:13px;letter-spacing:4.2px;margin-top:4px}
  .headline{
    position:absolute;left:0;top:161px;width:312px;height:123px;
    background:var(--charcoal);color:var(--white);
    display:flex;align-items:center;justify-content:center;text-align:center;
    font-size:21px;font-weight:500;line-height:1.3;letter-spacing:.4px;
  }
  .intro{position:absolute;left:44px;right:44px;top:368px;font-size:10.4px;line-height:1.32;text-align:justify}
  .intro p+p{margin-top:12px}
  .services{
    position:absolute;left:0;top:527px;width:560px;height:152px;background:var(--band);
    list-style:none;padding-top:12px;text-align:center;
  }
  .services li{font-size:12.4px;font-weight:600;line-height:18px;color:#33373b}
  .services li::before{content:"•";color:var(--teal-deep);margin-right:4px}
  .credentials{
    position:absolute;left:0;top:679px;width:560px;height:41px;
    display:flex;justify-content:center;align-items:center;gap:40px;
    font-size:13px;font-weight:600;color:var(--teal-deep);background:#f6f7f7;
  }
  .credentials span::before{content:"•";color:var(--navy);margin-right:5px}
  .contact{
    position:absolute;left:0;top:720px;width:560px;height:72px;
    background:linear-gradient(90deg,var(--teal) 0%,#2a8f8a 45%,var(--navy) 100%);
    color:var(--white);text-align:center;padding-top:9px;
  }
  .contact-phone{font-size:21px;font-weight:500;letter-spacing:.8px;display:block}
  .contact-web{font-size:15px;font-weight:500;display:block;margin-top:4px}
</style>
</head>
<body>
<main class="flyer">
  <svg class="hero-art" width="560" height="320" viewBox="0 0 560 320">
    <defs>
      <linearGradient id="stripe-grad" x1="0" y1="0" x2="0" y2="1">
        <stop offset="0" stop-color="#1e3a4d"/>
        <stop offset=".5" stop-color="#1f8c88"/>
        <stop offset="1" stop-color="#3fd19a"/>
      </linearGradient>
      <linearGradient id="photo-grad" x1="0" y1="0" x2="1" y2="1">
        <stop offset="0" stop-color="#f2f4f5"/>
        <stop offset=".55" stop-color="#cfd8de"/>
        <stop offset="1" stop-color="#a9b6bf"/>
      </linearGradient>
      <linearGradient id="corner-grad" x1="0" y1="1" x2="1" y2="0">
        <stop offset="0" stop-color="#3fd19a"/>
        <stop offset="1" stop-color="#1e3a4d"/>
      </linearGradient>
    </defs>
    <polygon class="accent-stripe" points="322,0 352,0 240,312 208,312" fill="url(#stripe-grad)"/>
    <polygon class="hero-photo" role="img" aria-label="Photo of a bookkeeper at her desk reviewing documents with a pen" points="352,0 560,0 560,312 240,312" fill="url(#photo-grad)"/>
    <polygon class="accent-corner" points="218,312 300,312 300,250" fill="url(#corner-grad)"/>
  </svg>

  <div class="brand">
    <span class="brand-mark"></span>
    <span class="brand-name">EVEN KEEL</span>
    <span class="brand-sub">Financial Services</span>
  </div>

  <h1 class="headline">BOOKKEEPING<br>TAILORED TO YOUR<br>BUSINESS NEEDS</h1>

  <section class="intro">
    <p>Are you a small business owner, tradie or PAVC Service Provider struggling to stay on top of your bookkeeping and compliance obligations? If so we would love to help you get back on track and take control of your business finances so that you can make informed business decisions and focus on what you do best.</p>
    <p>We have over 20 years industry experience and, as a small business ourselves, we are able to offer our clients a personal bookkeeping solution tailored to meet the needs of your business.</p>
  </section>

  <ul class="services">
    <li>Accounts Payable | Accounts Receivable</li>
    <li>Customer Invoicing</li>
    <li>Bank and Credit Card Reconciliations</li>
    <li>Payroll | Superannuation | Payroll Tax</li>
    <li>Business Activity | Instalment Activity Statements</li>
    <li>Regular Financial Reports</li>
    <li>Ledgra and Tallybooks Set-Up and Training</li>
  </ul>

  <div class="credentials">
    <span>Ledgra Certified Advisor</span>
    <span>Tallybooks Pro Advisor</span>
  </div>

  <footer class="contact">
    <span class="contact-phone">0400 318 752</span>
    <span class="contact-web">www.evenkeelfinancialservices.com.au</span>
  </footer>
</main>
</body>
</html>
```